Rise Civic Youth Website Re-design

The goal of this website redesign is to give Rise Civic Youth, a nonprofit focused on recruiting conservative candidates for public office to state and local positions, a platform that balances youthful energy with a sense of maturity and credibility. This site should not only inspire young conservatives across the country to get involved but also position the organization as a leader in cultivating the next generation of public servants. A clean, professional layout will convey trustworthiness, while bold visuals, clean animations, and design motifs will reinforce the patriotic and dynamic nature of the brand. Central to this design is an interactive or static map showcasing our Rising Stars from across the nation as the main home page, helping users quickly understand the breadth of the movement. See design brief for more.

Target Market(s)

18-35 year old American political conservatives

Coding

Coded - Design and coding required

Number of Pages Required

5+ page

Font styles to use
Sans Serif

Requirements
Nice to have
• An active or Static map that is representative of our membership. We will provide data but an example will do

```html
<!DOCTYPE html>
<html lang="en">
<head>
<meta charset="utf-8">
<title>Rise Civic Youth</title>
<link href="https://fonts.googleapis.com/css2?family=Montserrat:ital,wght@0,600;0,700;1,700&family=Poppins:wght@400;500;600&display=swap" rel="stylesheet">
<style>
:root{
  --navy:#1a1f71;
  --red:#b3173a;
  --ink:#111;
  --grey-bg:#f4f4f4;
  --field:#f2f2f2;
  --grad-start:#a83c5e;
  --grad-end:#2c3993;
  --white:#fff;
  --accent-lilac:#a9a4f5;
}
*{margin:0;padding:0;box-sizing:border-box}
html,body{width:1200px;height:3347px;overflow:hidden}
body{position:relative;font-family:'Poppins',sans-serif;color:var(--ink);background:var(--white)}
.abs{position:absolute}

/* Hero */
.hero{left:0;top:0;width:1200px;height:905px;
  background:linear-gradient(90deg,#cf6483 0%,#9c3f7c 30%,#5f2f8a 55%,#3b3aa0 80%,#2f3da5 100%)}
.hero-shade{left:0;top:0;width:1200px;height:905px;background:linear-gradient(180deg,rgba(20,10,60,.15),rgba(20,10,60,0) 40%,rgba(20,10,60,.2))}
.brand{left:97px;top:28px;font-family:'Montserrat',sans-serif;font-weight:700;font-size:22px;color:var(--white);line-height:1.15;width:130px}
.brand-dot{display:inline-block;width:10px;height:10px;border-radius:50%;background:var(--white);margin-right:6px;vertical-align:middle}
.main-nav{left:301px;top:36px;display:flex;gap:18px;font-weight:600;font-size:13.5px;color:var(--white);letter-spacing:-.1px}
.main-nav a{color:inherit;text-decoration:none}
.main-nav a.active{border-bottom:1.5px solid var(--white);padding-bottom:2px}
.hero-title{left:0;top:440px;width:1200px;text-align:center;font-family:'Montserrat',sans-serif;font-weight:700;font-size:43px;line-height:46px;color:var(--white)}
.hero-title em{color:var(--accent-lilac);font-style:italic}
.btn{display:flex;align-items:center;justify-content:center;gap:8px;font-weight:600;font-size:13px;text-transform:uppercase}
.btn-donate{left:523px;top:625px;width:154px;height:46px;background:var(--white);color:var(--ink)}

/* Section headings */
.section-title{left:0;width:1200px;text-align:center;font-family:'Montserrat',sans-serif;font-weight:700;font-size:44px;line-height:50px}
.section-title span{color:var(--navy)}
.rule{left:546px;width:108px;height:3px;background:var(--red)}
.body-copy{left:195px;width:810px;text-align:center;font-size:15.5px;line-height:26px;color:#222}

/* Rising stars */
.stars-bg{left:0;top:1300px;width:1200px;height:760px;background:var(--grey-bg)}
.star-card{height:62px;width:180px;border:1.3px solid var(--red);border-radius:6px;background:var(--white);
  display:flex;align-items:center;padding-left:38px;font-weight:500;font-size:14.5px}
.star-card.featured{border-color:var(--navy);box-shadow:0 4px 10px rgba(26,31,113,.2)}
.avatar{width:48px;height:48px;border-radius:50%;background:linear-gradient(135deg,#d9b49a,#7a5a48)}
.map{left:273px;top:1574px;width:714px;height:440px;border-radius:24px;
  background:radial-gradient(circle at 50% 50%,#cfcfcf 0%,#e2e2e2 60%,var(--grey-bg) 100%)}

/* Vision */
.vision{left:0;top:2060px;width:1200px;height:348px;background:linear-gradient(90deg,var(--grad-start),var(--grad-end))}
.vision-title{color:var(--white)}
.vision .rule,.rule.light{background:var(--white)}
.vision-copy{color:var(--white)}

/* Form */
.field{background:var(--field);height:66px;display:flex;align-items:center;padding-left:22px;font-size:13.5px;color:#333}
.btn-submit{left:523px;top:2831px;width:154px;height:46px;color:var(--white);background:linear-gradient(90deg,var(--grad-start),var(--grad-end))}

/* Footer */
.footer{left:0;top:3032px;width:1200px;height:315px;background:#000}
.footer-brand{left:0;top:3076px;width:1200px;text-align:center;font-family:'Montserrat',sans-serif;font-weight:700;font-size:26px;color:var(--white)}
.footer-nav{left:0;top:3170px;width:1200px;display:flex;justify-content:center;gap:18px;font-weight:600;font-size:13.5px;color:var(--white)}
.footer-social{left:0;top:3213px;width:1200px;text-align:center;font-size:13px;color:var(--white)}
.copyright{left:0;top:3256px;width:1200px;text-align:center;font-size:14px;color:var(--white)}
</style>
</head>
<body>

<!-- Hero -->
<div class="abs hero" role="img" aria-label="Photo of smiling children holding small American flags, with a pink-to-blue colour wash"></div>
<div class="abs hero-shade"></div>
<div class="abs brand"><span class="brand-dot"></span>Rise Civic Youth</div>
<nav class="abs main-nav">
  <a class="active" href="#">HOME</a><a href="#">ABOUT</a><a href="#">WHY LEADERSHIP</a><a href="#">RISING STARS</a>
  <a href="#">BECOME A LEADER</a><a href="#">BECOME A MENTOR</a><a href="#">PRESS</a><a href="#">CONTACT</a>
</nav>
<h1 class="abs hero-title">Empowering, Recruiting, &amp;<br>Mentoring <em>The Next Generation</em><br>of Conservative Leaders</h1>
<a class="abs btn btn-donate">Donate Now
  <svg width="14" height="8" viewBox="0 0 14 8"><path d="M0 4h12M9 1l3 3-3 3" stroke="#111" stroke-width="1.6" fill="none"/></svg></a>

<svg class="abs" style="left:0;top:860px" width="1200" height="120" viewBox="0 0 1200 120">
  <path d="M0 45 L240 38 C500 20 700 10 900 30 C1030 42 1130 60 1200 80 L1200 120 L0 120 Z" fill="#fff"/>
  <path d="M180 27 C260 20 330 22 378 30 C320 34 250 33 180 27 Z" fill="#000"/>
  <path d="M0 62 L240 75 C160 80 60 84 0 88 Z" fill="#7a2e5c"/>
  <path d="M1060 50 C1120 52 1170 56 1200 60 L1200 80 C1160 68 1110 58 1060 50 Z" fill="#34409b"/>
</svg>

<!-- Mission -->
<h2 class="abs section-title" style="top:998px">Our <span>Mission</span></h2>
<div class="abs rule" style="top:1059px"></div>
<p class="abs body-copy" style="top:1088px">Our vision is to prepare Generation Z leaders to take action, take charge, and take control of the future by supporting the vision of the founders of this country. We help them promote conservative political values such as limited government, free market capitalism, individual responsibility, and fiscal restraint.</p>

<!-- Rising stars -->
<div class="abs stars-bg"></div>
<svg class="abs" style="left:0;top:1255px" width="1200" height="90" viewBox="0 0 1200 90">
  <path d="M0 78 C250 40 520 14 760 10 C900 8 1060 18 1200 30 L1200 90 L0 90 Z" fill="#f4f4f4"/>
  <path d="M820 22 C920 25 1050 30 1200 40 L1200 46 C1080 38 940 30 820 22 Z" fill="#f4f4f4"/>
</svg>
<h2 class="abs section-title" style="top:1362px">RISING <span>STARS</span></h2>
<div class="abs rule" style="top:1422px"></div>

<div class="abs star-card" style="left:25px;top:1478px">Ethan Alvarez</div>
<div class="abs avatar" style="left:0;top:1485px" role="img" aria-label="Portrait of Ethan Alvarez"></div>
<div class="abs star-card" style="left:228px;top:1497px">Clara Conway</div>
<div class="abs avatar" style="left:203px;top:1504px" role="img" aria-label="Portrait of Clara Conway"></div>
<div class="abs star-card" style="left:431px;top:1481px;padding-left:24px">Camila Ashford</div>
<div class="abs avatar" style="left:406px;top:1488px" role="img" aria-label="Portrait of Camila Ashford"></div>
<div class="abs star-card featured" style="left:635px;top:1497px;padding-left:28px">Avery Langford</div>
<div class="abs avatar" style="left:609px;top:1504px" role="img" aria-label="Portrait of Avery Langford"></div>
<div class="abs star-card" style="left:838px;top:1481px;padding-left:32px">Tessa Caldwell</div>
<div class="abs avatar" style="left:812px;top:1488px" role="img" aria-label="Portrait of Tessa Caldwell"></div>
<div class="abs star-card" style="left:1041px;top:1494px;padding-left:46px">Tyler Brandt</div>
<div class="abs avatar" style="left:1015px;top:1501px" role="img" aria-label="Portrait of Tyler Brandt"></div>

<div class="abs map" role="img" aria-label="Dotted map of the United States marking Rising Star member locations"></div>

<!-- Vision -->
<div class="abs vision"></div>
<svg class="abs" style="left:0;top:2015px" width="1200" height="110" viewBox="0 0 1200 110">
  <defs><linearGradient id="visionGrad" x1="0" x2="1"><stop offset="0" stop-color="#a83c5e"/><stop offset="1" stop-color="#2c3993"/></linearGradient></defs>
  <path d="M0 58 L240 50 C420 28 620 12 820 20 C980 28 1100 40 1200 56 L1200 110 L0 110 Z" fill="url(#visionGrad)"/>
  <path d="M185 40 C260 33 330 35 380 43 C310 46 240 45 185 40 Z" fill="#6e2b62"/>
  <path d="M0 68 L245 78 C160 84 60 90 0 95 Z" fill="#fff"/>
</svg>
<h2 class="abs section-title vision-title" style="top:2146px;left:-26px">Our Vision</h2>
<div class="abs rule light" style="top:2205px;left:520px"></div>
<p class="abs body-copy vision-copy" style="top:2243px">Our vision is to prepare Generation Z leaders to take action, take charge, and take control of the future by supporting the vision of the founders of this country. We help them promote conservative political values such as limited government, free market capitalism, individual responsibility, and fiscal restraint.</p>

<!-- Get connected -->
<h2 class="abs section-title" style="top:2474px">GET <span>CONNECTED</span></h2>
<div class="abs rule" style="top:2533px"></div>
<form>
  <div class="abs field" style="left:225px;top:2578px;width:363px">FIRST NAME</div>
  <div class="abs field" style="left:611px;top:2578px;width:363px">LAST NAME</div>
  <div class="abs field" style="left:225px;top:2664px;width:363px">EMAIL</div>
  <div class="abs field" style="left:611px;top:2664px;width:363px">CITY, STATE</div>
  <div class="abs field" style="left:225px;top:2745px;width:749px">ADDRESS</div>
  <a class="abs btn btn-submit">Submit
    <svg width="14" height="8" viewBox="0 0 14 8"><path d="M0 4h12M9 1l3 3-3 3" stroke="#fff" stroke-width="1.6" fill="none"/></svg></a>
</form>

<!-- Footer -->
<svg class="abs" style="left:0;top:2950px" width="1200" height="90" viewBox="0 0 1200 90">
  <path d="M0 82 C250 48 520 22 840 14 C920 13 990 16 1005 22 C960 28 950 32 945 36 C1040 42 1130 50 1200 58 L1200 90 L0 90 Z" fill="#000"/>
</svg>
<div class="abs footer"></div>
<div class="abs footer-brand">Rise Civic Youth</div>
<nav class="abs footer-nav">
  <span>HOME</span><span>ABOUT</span><span>WHY LEADERSHIP</span><span>RISING STARS</span><span>BECOME A LEADER</span><span>BECOME A MENTOR</span><span>PRESS</span><span>CONTACT</span>
</nav>
<div class="abs footer-social">TOWNSQUARE | PIXLANE | LINKWORK | CHIRPLINE</div>
<div class="abs copyright">Copyright@2025.All Rights Reserved</div>

</body>
</html>
```